Homepage design change needed

We're looking for a designer to change the way our homepage looks according to the attached sketch along with the project brief below.
Existing website is: http://www.tallowmere.co.nz
Please download the sketched design from the link below. https://www.parcelvoxa.com/s/k3m9q2x7t4w1z8r/fwdwebsitedesignneeded2.zip
There are 4 images inside the above zip file. front1, 2 & 3 make up the homepage.
page2.jpg is a sketch of what we'd like instead of the current page http://www.tallowmere.co.nz/join-tallowmere.aspx
Requirements
Must have
- The design must keep the following elements the same as the existing website:
- colour scheme
- same width
- same rounded corners/soft edges
- rounded buttons
- the graphics look of the following video brought through into the illustrations http://www.tallowmere.co.nz/help/video.aspx
front1.jpg - there is an illustration (3 boxes with = success! written); please don't design an illustration, simply leave space for a graphic to be put in its place later.
front2 and 3.jpg are to be fully designed as sketched. (again please ignore the illustration with 3 boxes = success!)

```html
<!DOCTYPE html>
<html lang="en">
<head>
<meta charset="utf-8">
<title>Quorrelby – Home</title>
<link href="https://fonts.googleapis.com/css2?family=Raleway:wght@300;400;500;600;700&display=swap" rel="stylesheet">
<style>
:root{
  --blue:#0f8cff;
  --blue-dark:#0a5fae;
  --blue-line:#9fcdf5;
  --canvas:#ebebeb;
  --white:#ffffff;
  --bubble:#ececec;
}
*{box-sizing:border-box;margin:0;padding:0}
html,body{width:1200px;height:2347px;overflow:hidden;background:var(--canvas);font-family:"Raleway",sans-serif;color:var(--blue)}
.stage{position:relative;width:1200px;height:2347px}
.abs{position:absolute}
.page{left:77px;top:33px;width:1047px;height:2235px;background:var(--white);border:1px solid var(--blue-line)}
.brand{left:0;width:1200px;top:70px;text-align:center;font-size:31px;font-weight:700;color:var(--blue);letter-spacing:.5px}
.band{left:55px;width:1090px;background:var(--blue);color:var(--white)}
.fold{fill:var(--blue-dark)}
.band-hero{top:150px;height:133px;text-align:center;font-size:26px;font-weight:300;line-height:39px;padding-top:30px}
h2{font-weight:400;font-size:26px;color:var(--blue)}
.list{list-style:none;font-size:20px;line-height:26px}
.list li{position:absolute;left:0;padding-left:46px;white-space:nowrap}
.list li svg{position:absolute;left:0;top:4px}
.btn{display:flex;align-items:center;justify-content:space-between;background:var(--blue);color:var(--white);border-radius:4px;font-weight:700;font-size:15px;line-height:22px;letter-spacing:.6px;padding:0 14px 0 17px;text-decoration:none}
.btn.light{background:var(--white);color:var(--blue)}
.btn.small{font-size:12px;line-height:17px;font-weight:600;letter-spacing:0;padding:0 10px}
.link{color:var(--blue);text-decoration:underline;font-size:17px;line-height:24px;text-align:center}
.rule{height:1px;background:var(--blue-line)}
.frame{width:240px;height:240px;border:1.5px solid var(--blue);border-radius:4px}
.success{font-size:20px;font-weight:700}
.label{font-size:20px;font-weight:600;width:240px;text-align:center}
.band-mid{top:1080px;height:208px}
.band-mid p{position:absolute;left:65px;font-size:22px;font-weight:600}
.band-mid .link{color:var(--white)}
h3{font-size:23px;font-weight:600}
.bubble{width:196px;height:140px}
.bubble svg{position:absolute;left:0;top:0}
.bubble p{position:absolute;left:27px;top:12px;width:138px;font-size:12.5px;line-height:19.7px;color:var(--blue)}
.name{font-size:15px}
.search-box{width:238px;height:42px;border:1.5px solid var(--blue);border-radius:4px}
.cats{font-size:13px;font-weight:600;line-height:26.5px}
.thumb{width:86px;height:59px;background:var(--blue);border-radius:3px}
.meta{font-size:11.5px;font-weight:600;line-height:19.7px}
.footer{left:77px;width:1047px;top:2073px;height:195px;background:var(--blue);color:var(--white)}
.logo-slot{width:117px;height:47px;background:var(--white);border-radius:3px;color:var(--blue);font-size:18px;display:flex;align-items:center;justify-content:center}
.note{font-size:12px}
</style>
</head>
<body>
<div class="stage">
  <div class="abs page"></div>
  <div class="abs brand">quorrelby.co.nz</div>

  <svg class="abs" style="left:55px;top:130px" width="1090" height="20"><polygon class="fold" points="0,20 22,0 22,20"/><polygon class="fold" points="1090,20 1068,0 1068,20"/></svg>
  <div class="abs band band-hero">The place to hire and be hired putting you<br>in the driver seat (where you belong).</div>

  <h2 class="abs" style="left:119px;top:312px">I want to be hired</h2>
  <h2 class="abs" style="left:641px;top:312px">I want to hire someone</h2>

  <ul class="abs list" style="left:122px;top:382px">
    <li style="top:0"><svg width="26" height="20"><path d="M3 10l7 7L23 3" fill="none" stroke="#0f8cff" stroke-width="4"/></svg>Advertise yourself in your own words</li>
    <li style="top:53px"><svg width="26" height="20"><path d="M3 10l7 7L23 3" fill="none" stroke="#0f8cff" stroke-width="4"/></svg>Employers approach you directly</li>
    <li style="top:105px"><svg width="26" height="20"><path d="M3 10l7 7L23 3" fill="none" stroke="#0f8cff" stroke-width="4"/></svg>Accept job offers, create extra income<br>on your own terms</li>
  </ul>
  <ul class="abs list" style="left:645px;top:382px">
    <li style="top:0"><svg width="26" height="20"><path d="M3 10l7 7L23 3" fill="none" stroke="#0f8cff" stroke-width="4"/></svg>Search profiles for free</li>
    <li style="top:53px"><svg width="26" height="20"><path d="M3 10l7 7L23 3" fill="none" stroke="#0f8cff" stroke-width="4"/></svg>Connect people directly for free</li>
    <li style="top:105px"><svg width="26" height="20"><path d="M3 10l7 7L23 3" fill="none" stroke="#0f8cff" stroke-width="4"/></svg>Immeadiate access to thousands<br>of people</li>
  </ul>

  <a class="abs btn" style="left:239px;top:593px;width:176px;height:59px" href="#">CREATE YOUR<br>PROFILE NOW<svg width="14" height="24"><path d="M2 2l9 10-9 10" fill="none" stroke="#fff" stroke-width="3"/></svg></a>
  <div class="abs link" style="left:500px;top:598px;width:200px;text-decoration:none">or <u>see how</u><br><u>Quorrelby works</u></div>
  <a class="abs btn" style="left:763px;top:601px;width:174px;height:42px" href="#">SEARCH NOW<svg width="24" height="24"><circle cx="9" cy="9" r="6.5" fill="none" stroke="#fff" stroke-width="3"/><path d="M14 14l7 7" stroke="#fff" stroke-width="3.5"/></svg></a>

  <div class="abs rule" style="left:191px;top:685px;width:818px"></div>

  <div class="abs frame" style="left:120px;top:721px" role="img" aria-label="Space for the 'Immediate' graphic"></div>
  <svg class="abs" style="left:371px;top:830px" width="22" height="22"><path d="M11 2v18M2 11h18" stroke="#0f8cff" stroke-width="3.5"/></svg>
  <div class="abs frame" style="left:404px;top:721px" role="img" aria-label="Space for the 'Easy' graphic"></div>
  <svg class="abs" style="left:655px;top:830px" width="22" height="22"><path d="M11 2v18M2 11h18" stroke="#0f8cff" stroke-width="3.5"/></svg>
  <div class="abs frame" style="left:688px;top:721px" role="img" aria-label="Space for the 'Free' graphic"></div>
  <div class="abs success" style="left:950px;top:829px">= SUCCESS !</div>
  <div class="abs label" style="left:120px;top:985px">Immediate</div>
  <div class="abs label" style="left:404px;top:985px">Easy</div>
  <div class="abs label" style="left:688px;top:985px">Free</div>
  <a class="abs btn" style="left:906px;top:997px;width:174px;height:59px" href="#">CREATE YOUR<br>PROFILE NOW<svg width="14" height="24"><path d="M2 2l9 10-9 10" fill="none" stroke="#fff" stroke-width="3"/></svg></a>

  <div class="abs band band-mid">
    <p style="top:24px">Create flexible income on your own terms.</p>
    <p style="top:63px">Quorrelby is not just for job seekers. Be hired by someone in your own community.</p>
    <a class="abs link" style="left:384px;top:141px;width:320px" href="#">see how Quorrelby works</a>
    <a class="abs btn light" style="left:851px;top:125px;width:174px;height:59px" href="#">CREATE YOUR<br>PROFILE NOW<svg width="14" height="24"><path d="M2 2l9 10-9 10" fill="none" stroke="#0f8cff" stroke-width="3"/></svg></a>
  </div>
  <svg class="abs" style="left:55px;top:1288px" width="1090" height="21"><polygon class="fold" points="0,0 22,0 22,21"/><polygon class="fold" points="1090,0 1068,0 1068,21"/></svg>

  <h3 class="abs" style="left:120px;top:1310px">Quorrelby works !</h3>

  <div class="abs bubble" style="left:152px;top:1362px">
    <svg width="196" height="140"><path d="M30 2h140a20 20 0 0 1 20 20v70a20 20 0 0 1-20 20H62L4 136l28-24H30a20 20 0 0 1-20-20V22A20 20 0 0 1 30 2z" fill="#ececec" stroke="#0f8cff" stroke-width="1.5"/></svg>
    <p>Proin gravida nibh vel velit auctor aliquet. Aenean sollicitudin, lorem quis bibendum</p>
  </div>
  <div class="abs bubble" style="left:382px;top:1362px">
    <svg width="196" height="140"><path d="M30 2h140a20 20 0 0 1 20 20v70a20 20 0 0 1-20 20H62L4 136l28-24H30a20 20 0 0 1-20-20V22A20 20 0 0 1 30 2z" fill="#ececec" stroke="#0f8cff" stroke-width="1.5"/></svg>
    <p>Duis sed odio sit nisi elit consequat ipsum, nec sagittis sem nibh id elit.</p>
  </div>
  <div class="abs bubble" style="left:617px;top:1362px">
    <svg width="196" height="140"><path d="M30 2h140a20 20 0 0 1 20 20v70a20 20 0 0 1-20 20h-6l28 24-58-24H30a20 20 0 0 1-20-20V22A20 20 0 0 1 30 2z" fill="#ececec" stroke="#0f8cff" stroke-width="1.5"/></svg>
    <p>Class aptent taciti sociosqu ad litora torquent per conubia nostra, per inceptos</p>
  </div>
  <div class="abs bubble" style="left:846px;top:1362px">
    <svg width="196" height="140"><path d="M30 2h140a20 20 0 0 1 20 20v70a20 20 0 0 1-20 20H62L4 136l28-24H30a20 20 0 0 1-20-20V22A20 20 0 0 1 30 2z" fill="#ececec" stroke="#0f8cff" stroke-width="1.5"/></svg>
    <p>Etiam ut imperdiet nisi. Proin condimentum fermentum nunc.</p>
  </div>
  <div class="abs name" style="left:119px;top:1512px">Hemi Walsh</div>
  <div class="abs name" style="left:347px;top:1512px">Ana Roberts</div>
  <div class="abs name" style="left:723px;top:1512px">Miriama Cole</div>
  <div class="abs name" style="left:951px;top:1512px">Liam Doyle</div>

  <a class="abs btn" style="left:513px;top:1565px;width:174px;height:59px" href="#">CREATE YOUR<br>PROFILE NOW<svg width="14" height="24"><path d="M2 2l9 10-9 10" fill="none" stroke="#fff" stroke-width="3"/></svg></a>

  <div class="abs rule" style="left:191px;top:1657px;width:818px"></div>

  <h3 class="abs" style="left:120px;top:1681px;font-size:21px">Search profiles now</h3>
  <div class="abs search-box" style="left:120px;top:1737px"></div>
  <svg class="abs" style="left:368px;top:1746px" width="26" height="26"><circle cx="10" cy="10" r="7" fill="none" stroke="#0f8cff" stroke-width="3.5"/><path d="M15 15l8 8" stroke="#0f8cff" stroke-width="4"/></svg>

  <h3 class="abs" style="left:120px;top:1817px;font-size:20px;font-weight:400">Work categories</h3>
  <div class="abs cats" style="left:120px;top:1855px">Lorem ipsum dolor<br>Lorem ipsum dolor<br>Lorem ipsum dolor<br>Lorem ipsum dolor</div>
  <div class="abs cats" style="left:294px;top:1855px">Lorem ipsum dolor<br>Lorem ipsum dolor<br>Lorem ipsum dolor<br>Lorem ipsum dolor</div>
  <a class="abs btn small" style="left:408px;top:1990px;width:116px;height:49px" href="#">more work<br>categories<svg width="14" height="10"><path d="M2 2l5 5 5-5" fill="none" stroke="#fff" stroke-width="2"/></svg></a>

  <div class="abs thumb" style="left:579px;top:1737px" role="img" aria-label="Profile photo"></div>
  <div class="abs meta" style="left:687px;top:1734px">Lorem ipsum dolor<br>Lorem ipsum dolor<br>Lorem ipsum dolor</div>
  <div class="abs thumb" style="left:829px;top:1737px" role="img" aria-label="Profile photo"></div>
  <div class="abs meta" style="left:937px;top:1734px">Lorem ipsum dolor<br>Lorem ipsum dolor<br>Lorem ipsum dolor</div>
  <div class="abs thumb" style="left:579px;top:1824px" role="img" aria-label="Profile photo"></div>
  <div class="abs meta" style="left:687px;top:1821px">Lorem ipsum dolor<br>Lorem ipsum dolor<br>Lorem ipsum dolor</div>
  <div class="abs thumb" style="left:829px;top:1824px" role="img" aria-label="Profile photo"></div>
  <div class="abs meta" style="left:937px;top:1821px">Lorem ipsum dolor<br>Lorem ipsum dolor<br>Lorem ipsum dolor</div>
  <div class="abs thumb" style="left:579px;top:1912px" role="img" aria-label="Profile photo"></div>
  <div class="abs meta" style="left:687px;top:1909px">Lorem ipsum dolor<br>Lorem ipsum dolor<br>Lorem ipsum dolor</div>
  <div class="abs thumb" style="left:829px;top:1912px" role="img" aria-label="Profile photo"></div>
  <div class="abs meta" style="left:937px;top:1909px">Lorem ipsum dolor<br>Lorem ipsum dolor<br>Lorem ipsum dolor</div>
  <a class="abs btn small" style="left:982px;top:1990px;width:98px;height:49px" href="#">more<br>profiles<svg width="14" height="10"><path d="M2 2l5 5 5-5" fill="none" stroke="#fff" stroke-width="2"/></svg></a>

  <div class="abs footer">
    <h3 class="abs" style="left:43px;top:22px;font-size:22px">Employers using Quorrelby</h3>
    <svg class="abs" style="left:43px;top:92px" width="20" height="20"><circle cx="10" cy="10" r="10" fill="#fff"/><path d="M12 5l-6 5 6 5z" fill="#0f8cff"/></svg>
    <div class="abs logo-slot" style="left:89px;top:78px">Lorem</div>
    <div class="abs logo-slot" style="left:242px;top:78px">Ipsum</div>
    <div class="abs logo-slot" style="left:388px;top:78px">Lorem</div>
    <div class="abs logo-slot" style="left:541px;top:78px">Ipsum</div>
    <div class="abs logo-slot" style="left:688px;top:78px">Lorem</div>
    <div class="abs logo-slot" style="left:841px;top:78px">Ipsum</div>
    <svg class="abs" style="left:980px;top:92px" width="20" height="20"><circle cx="10" cy="10" r="10" fill="#fff"/><path d="M8 5l6 5-6 5z" fill="#0f8cff"/></svg>
    <div class="abs note" style="left:43px;top:145px">We actually send profiles to these and other employers</div>
  </div>
</div>
</body>
</html>
```